Real estate broker business card

Want a modern celan but effective business card for my residential and commercial real estate business. I want the back of the card to advertise my services and to capture business. I have attached the back of my current business card fore ideas

Target Market(s)

home buyers and seller. commercial buyers and sellers

Industry/Entity Type

Real Estate

Contact Information for Business Card

must have my contact information and my photo

Requirements
Must have
• Corla Vintreff
• Owner & Qualifying Broker
• Vintreff Real Estate Services
• 505.718.2947
• corla@vintreffhomes.com
• www.vintreffhomes.com
Nice to have
• metallic
• Business capture text: " Don't buy or lease property without someone looking out for your best interests. I will represent you on your home or investment purchase for FREE!"
• "Home owners, call today to receive a FREE market analysis for your homes value!

```html
<!DOCTYPE html>
<html lang="en">
<head>
<meta charset="utf-8">
<title>Vintreff Real Estate Services – Business Card</title>
<link href="https://fonts.googleapis.com/css2?family=Arimo:wght@400;700&display=swap" rel="stylesheet">
<style>
  :root {
    --backdrop: #3a3431;
    --card: #141516;
    --card-edge: #1c1d1f;
    --teal: #1f8a96;
    --teal-light: #3fb0bb;
    --silver: #c9cdd0;
    --muted: #9a9ea2;
    --divider: #5c6064;
    --photo-top: #4a5358;
    --photo-bottom: #2a3034;
  }
  * { box-sizing: border-box; margin: 0; padding: 0; }
  html, body {
    width: 1200px; height: 864px; overflow: hidden;
    background: var(--backdrop);
    font-family: "Arimo", Arial, sans-serif;
  }
  .canvas { position: relative; width: 1200px; height: 864px; }

  .card {
    position: absolute;
    width: 540px; height: 309px;
    background: var(--card);
    border: 1px solid var(--card-edge);
    box-shadow: 0 14px 30px rgba(0,0,0,.45);
  }
  .card--back  { left: 60px;  top: 150px; }
  .card--front { left: 600px; top: 405px; }

  .brand {
    position: absolute; left: 0; right: 0;
    display: flex; align-items: center; justify-content: center; gap: 12px;
  }
  .brand__mark {
    width: 18px; height: 18px; border-radius: 50%;
    background: var(--teal);
  }
  .brand__name {
    font-weight: 400; font-size: 38px;
    color: var(--silver);
  }
  .card--back .brand  { top: 60px; }
  .card--front .brand { top: 62px; }

  .pitch {
    position: absolute; left: 40px; right: 40px; top: 150px;
    text-align: center; color: var(--muted);
    font-size: 14px; line-height: 1.6;
  }

  .photo {
    position: absolute; left: 36px; top: 36px;
    width: 84px; height: 84px; border-radius: 50%;
    background: linear-gradient(180deg, var(--photo-top), var(--photo-bottom));
    border: 2px solid var(--divider);
  }

  .identity {
    position: absolute; right: 290px; top: 170px;
    text-align: right; color: var(--silver);
    font-size: 15px; line-height: 1.45;
  }
  .identity__name { color: var(--teal-light); font-size: 19px; font-weight: 700; margin-bottom: 2px; }

  .divider {
    position: absolute; left: 264px; top: 170px;
    width: 1px; height: 92px; background: var(--divider);
  }

  .contact {
    position: absolute; left: 282px; top: 174px;
    list-style: none; color: var(--silver); font-size: 14px;
  }
  .contact li { display: flex; align-items: center; gap: 9px; height: 22px; }
  .contact svg { width: 15px; height: 15px; flex: none; }
</style>
</head>
<body>
<main class="canvas">

  <section class="card card--back" aria-label="Card back">
    <div class="brand">
      <span class="brand__mark"></span>
      <span class="brand__name">Vintreff</span>
    </div>
    <p class="pitch">
      Don't buy or lease property without someone<br>
      looking out for your best interests.<br>
      I will represent you on your home or investment purchase for FREE!
    </p>
  </section>

  <section class="card card--front" aria-label="Card front">
    <div class="photo" role="img" aria-label="Portrait photo of Corla Vintreff"></div>

    <div class="brand">
      <span class="brand__mark"></span>
      <span class="brand__name">Vintreff</span>
    </div>

    <div class="identity">
      <p class="identity__name">Corla Vintreff</p>
      <p>Owner &amp; Qualifying Broker</p>
      <p>Vintreff Real Estate Services</p>
    </div>

    <span class="divider"></span>

    <ul class="contact">
      <li>
        <svg viewBox="0 0 16 16" aria-hidden="true"><path fill="#1f8a96" d="M4 1.5l2.3 3-1.4 1.6c.8 1.8 2.2 3.2 4 4l1.6-1.4 3 2.3-1.2 2.5C7 13.3 2.7 9 2.2 3.2z"/></svg>
        505.718.2947
      </li>
      <li>
        <svg viewBox="0 0 16 16" aria-hidden="true"><rect x="1.5" y="3.5" width="13" height="9" rx="1" fill="#1f8a96"/><path d="M2 4.5l6 4.5 6-4.5" fill="none" stroke="#141516" stroke-width="1.3"/></svg>
        corla@vintreffhomes.com
      </li>
      <li>
        <svg viewBox="0 0 16 16" aria-hidden="true"><circle cx="8" cy="8" r="6.5" fill="#1f8a96"/><path d="M1.5 8h13M8 1.5c-2.4 2.6-2.4 10.4 0 13M8 1.5c2.4 2.6 2.4 10.4 0 13" fill="none" stroke="#141516" stroke-width="1"/></svg>
        www.vintreffhomes.com
      </li>
    </ul>
  </section>

</main>
</body>
</html>
```